Bolera Brisa

Website for a night club with live music and cabaret dancers. I would like to have the following Menu: 1.) Home; 2) The Facilities; 3) The Show; 4) Other Attractions; 5) Videos & Fotos; 6) Program; 7) Reservations; 8) Membership; 9) Contacts.

The pages should be easily editable and allow to enter text, including the menu since the final version will be in both English and Portuguese. It should have a toggle or links for the Portuguese language and the English Language.

The night club itself is called "BOLERA BRISA"; and its URL is www.bolerabrisa-example.com.

Industry/Entity Type

Night Club

```html
<!DOCTYPE html>
<html lang="en">
<head>
<meta charset="utf-8">
<title>Bolera Brisa — Night Club</title>
<link href="https://fonts.googleapis.com/css2?family=Roboto+Condensed:wght@400;700&family=Arimo:wght@400&display=swap" rel="stylesheet">
<style>
  :root {
    --red: #ee2a2c;
    --red-dark: #a3161a;
    --bg: #161616;
    --header-bg: #121212;
    --panel: #1c1c1c;
    --card: #0f0f0f;
    --footer: #0b0b0b;
    --white: #ffffff;
    --muted: #9a9a9a;
    --frame: #0c0c0c;
  }
  * { box-sizing: border-box; margin: 0; padding: 0; }
  html, body { width: 943px; height: 1200px; overflow: hidden; }
  body {
    position: relative;
    background: var(--bg);
    color: var(--white);
    font-family: "Arimo", Arial, sans-serif;
  }
  .abs { position: absolute; }

  .site-header { left: 0; top: 0; width: 943px; height: 88px; background: var(--header-bg); }
  .brand {
    left: 104px; top: 33px;
    font-family: "Roboto Condensed", sans-serif; font-weight: 700;
    font-size: 20px; letter-spacing: 0.2px; color: var(--white);
  }
  .search {
    left: 639px; top: 29px; width: 200px; height: 29px;
    border: 1px solid #9c9c9c; background: #0d0d0d;
    font-size: 9.5px; color: #dcdcdc; padding: 9px 9px;
  }
  .search svg { position: absolute; right: 10px; top: 8px; }

  .main-nav {
    left: 85px; top: 89px; width: 774px; height: 42px;
    background: var(--red);
    display: flex; justify-content: space-between; align-items: center;
    padding: 0 28px 0 30px;
    font-family: "Roboto Condensed", sans-serif; font-size: 10px; color: var(--white);
    list-style: none;
  }
  .fold { top: 131px; }

  .hero-frame { left: 103px; top: 131px; width: 737px; height: 375px; background: var(--frame); }
  .hero-media {
    left: 108px; top: 132px; width: 727px; height: 370px;
    background: linear-gradient(180deg, #4e4536 0%, #5c5040 55%, #4a5a52 100%);
  }
  .hero-arrow { top: 280px; }
  .hero-caption {
    left: 245px; top: 428px; width: 451px; height: 45px;
    background: var(--red);
    font-family: "Roboto Condensed", sans-serif; font-weight: 700;
    font-size: 18px; line-height: 45px; text-align: center;
  }

  .events-panel { left: 103px; top: 520px; width: 737px; height: 258px; background: var(--panel); }
  .section-title {
    font-family: "Roboto Condensed", sans-serif; font-weight: 700;
    font-size: 27px; line-height: 1; color: var(--white); white-space: nowrap;
  }
  .section-title em { font-style: normal; color: var(--red); }
  .events-title { left: 112px; top: 538px; }
  .pager { top: 541px; width: 20px; height: 20px; background: var(--red-dark); border: 1px solid #d44; }
  .pager svg { display: block; margin: 5px auto; }

  .event-card { top: 583px; width: 174px; height: 187px; background: var(--card); }
  .event-media { position: absolute; left: 6px; top: 6px; width: 163px; height: 135px; }
  .event-name {
    position: absolute; left: 0; top: 148px; width: 100%; text-align: center;
    font-family: "Roboto Condensed", sans-serif; font-size: 10.5px; color: var(--white);
  }
  .event-date {
    position: absolute; left: 0; top: 166px; width: 100%; text-align: center;
    font-family: "Roboto Condensed", sans-serif; font-size: 8.5px; color: var(--red);
  }

  .lower-panel { left: 103px; top: 816px; width: 737px; height: 270px; background: var(--panel); }
  .thumb { border: 2px solid var(--white); }
  .body-text { font-size: 8.7px; line-height: 15.5px; color: #e8e8e8; }
  .welcome-lead { left: 358px; top: 1003px; font-size: 8.3px; color: var(--muted); }
  .welcome-text { left: 358px; top: 1020px; width: 230px; }
  .news-date {
    font-family: "Roboto Condensed", sans-serif; font-weight: 700;
    font-size: 9.5px; color: var(--red);
  }
  .news-text { width: 132px; line-height: 16px; }

  .site-footer { left: 0; top: 1114px; width: 943px; height: 86px; background: var(--footer); }
  .copyright { left: 105px; top: 1153px; font-size: 8.8px; color: #f0f0f0; }
  .social { top: 1143px; width: 30px; height: 30px; border-radius: 50%; background: var(--white); }
</style>
</head>
<body>
  <header class="abs site-header"></header>
  <div class="abs brand">BOLERA BRISA</div>
  <div class="abs search">Search
    <svg width="13" height="13" viewBox="0 0 13 13"><circle cx="4.5" cy="4.5" r="3.3" fill="none" stroke="#fff" stroke-width="1.6"/><line x1="7" y1="7" x2="12" y2="12" stroke="#fff" stroke-width="2"/></svg>
  </div>

  <div class="abs hero-frame"></div>
  <svg class="abs fold" style="left:85px" width="19" height="16"><polygon points="0,0 19,0 19,16" fill="var(--red-dark)"/></svg>
  <svg class="abs fold" style="left:840px" width="19" height="16"><polygon points="0,0 19,0 0,16" fill="var(--red-dark)"/></svg>
  <ul class="abs main-nav">
    <li>HOME</li><li>THE FACILITIES</li><li>THE SHOW</li><li>OTHER ATTRACTIONS</li><li>VIDEOS &amp; FOTOS</li><li>PROGRAM</li><li>RESERVATIONS</li><li>MEMBERSHIP</li><li>CONTACTS</li>
  </ul>

  <div class="abs hero-media" role="img" aria-label="Photo of four smiling cabaret dancers in colourful feathered headdresses"></div>
  <svg class="abs hero-arrow" style="left:131px" width="18" height="72"><polyline points="16,1 2,36 16,71" fill="none" stroke="#fff" stroke-width="1.5"/></svg>
  <svg class="abs hero-arrow" style="left:795px" width="18" height="72"><polyline points="2,1 16,36 2,71" fill="none" stroke="#fff" stroke-width="1.5"/></svg>
  <div class="abs hero-caption">NIGHT CLUB WITH LIVE MUSIC AND CABARET DANCERS</div>

  <section class="abs events-panel"></section>
  <h2 class="abs section-title events-title">UPCOMING <em>EVENTS</em></h2>
  <div class="abs pager" style="left:790px"><svg width="6" height="10"><polyline points="5,1 1,5 5,9" fill="none" stroke="#fff" stroke-width="1.2"/></svg></div>
  <div class="abs pager" style="left:811px"><svg width="6" height="10"><polyline points="1,1 5,5 1,9" fill="none" stroke="#fff" stroke-width="1.2"/></svg></div>

  <article class="abs event-card" style="left:108px">
    <div class="event-media" role="img" aria-label="Photo of a woman dancing under club lights" style="background:linear-gradient(180deg,#6a3a8a,#8a4a7a)"></div>
    <p class="event-name">NEQUE PORRO QUISQUAM</p><p class="event-date">TUESDAY 25,2014</p>
  </article>
  <article class="abs event-card" style="left:292px">
    <div class="event-media" role="img" aria-label="Photo of dancers in pink stage light" style="background:linear-gradient(180deg,#c23a7a,#7a1a4a)"></div>
    <p class="event-name">NEQUE PORRO QUISQUAM</p><p class="event-date">TUESDAY 25,2014</p>
  </article>
  <article class="abs event-card" style="left:475px">
    <div class="event-media" role="img" aria-label="Photo of a crowd dancing at a bar" style="background:linear-gradient(180deg,#6a4a32,#4a2a24)"></div>
    <p class="event-name">NEQUE PORRO QUISQUAM</p><p class="event-date">TUESDAY 25,2014</p>
  </article>
  <article class="abs event-card" style="left:659px">
    <div class="event-media" role="img" aria-label="Photo of a group of women dancing by a DJ desk" style="background:linear-gradient(180deg,#9a8a82,#4a3034)"></div>
    <p class="event-name">NEQUE PORRO QUISQUAM</p><p class="event-date">TUESDAY 25,2014</p>
  </article>

  <section class="abs lower-panel"></section>
  <h2 class="abs section-title" style="left:117px;top:833px;font-size:23px">GALLER<em>Y</em></h2>
  <div class="abs thumb" role="img" aria-label="Gallery photo of friends taking a selfie" style="left:118px;top:877px;width:101px;height:91px;background:linear-gradient(180deg,#8a6a3a,#3a2a26)"></div>
  <div class="abs thumb" role="img" aria-label="Gallery photo of people cheering at a party" style="left:224px;top:877px;width:101px;height:91px;background:linear-gradient(180deg,#4a5070,#5a4a4e)"></div>
  <div class="abs thumb" role="img" aria-label="Gallery photo of a couple dancing" style="left:118px;top:973px;width:101px;height:91px;background:linear-gradient(180deg,#8a3a40,#3a2424)"></div>
  <div class="abs thumb" role="img" aria-label="Gallery photo of a concert crowd under lights" style="left:224px;top:973px;width:101px;height:91px;background:linear-gradient(180deg,#5a2a6a,#2a2440)"></div>

  <h2 class="abs section-title" style="left:354px;top:840px;font-size:23px">WELCOME <em>TO OUR SITE</em></h2>
  <div class="abs thumb" role="img" aria-label="Photo of cabaret dancers in feathered costumes with a drummer" style="left:357px;top:877px;width:225px;height:115px;background:linear-gradient(180deg,#7a4a3a,#3a4a3a)"></div>
  <p class="abs welcome-lead">LOREM IPSUM DOLOR SIT AMET, CONSECTETUR</p>
  <p class="abs body-text welcome-text">Lorem ipsum dolor sit amet, consectetur adipiscing elit. Maecenas vitae pellentesque mi. Aliquam erat volutpat. Morbi et nisi id neque tincidunt dapibus.</p>

  <h2 class="abs section-title" style="left:612px;top:840px;font-size:23px">LATEST <em>NEWS</em></h2>
  <div class="abs thumb" role="img" aria-label="News photo of women at a party" style="left:614px;top:878px;width:76px;height:70px;background:linear-gradient(180deg,#8a5a5a,#3a2230)"></div>
  <p class="abs news-date" style="left:703px;top:879px">TUE, SEP 04</p>
  <p class="abs body-text news-text" style="left:703px;top:900px">Donec faucibus orci sit amet ipsum pulvinar interdum. Vivmus vehicula lorem sit amet augue</p>
  <div class="abs thumb" role="img" aria-label="News photo of a woman singing" style="left:614px;top:973px;width:76px;height:70px;background:linear-gradient(180deg,#a0703a,#4a3226)"></div>
  <p class="abs news-date" style="left:703px;top:974px">TUE, SEP 04</p>
  <p class="abs body-text news-text" style="left:703px;top:994px">Donec faucibus orci sit amet ipsum pulvinar interdum. Vivmus vehicula lorem sit amet augue</p>

  <footer class="abs site-footer"></footer>
  <p class="abs copyright">© Copy Right 2014 Bolera Brisa.All Right reserved.</p>
  <div class="abs social" style="left:592px" aria-label="Social link"></div>
  <div class="abs social" style="left:628px" aria-label="Social link"></div>
  <div class="abs social" style="left:664px" aria-label="Social link"></div>
  <div class="abs social" style="left:701px" aria-label="News feed"></div>
  <div class="abs social" style="left:737px" aria-label="Video channel"></div>
  <div class="abs social" style="left:773px" aria-label="Social link"></div>
  <div class="abs social" style="left:810px" aria-label="Social link"></div>
</body>
</html>
```